Book dust cover- front and back- 5.5x 8.5, white back ground, simple, testimonial on the back (just use sample words) price, qr code and picture of author. Front will include title and tagline
Tagline- The 7 Mindsets to Overcome Life's Challenges
Sorry, it didn't ask me specifically for everything.
Title: Walking Into Amber Light
Tagline: Seven Truths for Rising Above Life's Storms
Christian based- I use scripture and science to prove each mindset
No pink or girly looks
I like the covers like: Derek T Halloway's Books, Ironwilled, Fig and Kettle (words with little imagery- unless it really makes sense)
Females- 25-65
Christian

```html
<!DOCTYPE html>
<html lang="en">
<head>
<meta charset="utf-8">
<title>Walking Into Amber Light – Cover Wrap</title>
<link rel="stylesheet" href="https://fonts.googleapis.com/css2?family=Playfair+Display:wght@700;900&family=Cinzel:wght@400;600&family=EB+Garamond:ital,wght@0,400;1,400&display=swap">
<style>
  :root{
    --canvas:#efefef;
    --paper:#ffffff;
    --ink:#161616;
    --band-top:#2a2a2a;
    --band-bottom:#0c0c0c;
    --gold:#c9a86a;
    --gold-deep:#9c7a3f;
    --body:#3a3a3a;
    --edge:#e4e4e4;
  }
  *{margin:0;padding:0;box-sizing:border-box}
  html,body{width:900px;height:1200px;overflow:hidden;background:var(--canvas)}
  .cover-wrap{
    position:absolute;left:20px;top:285px;width:860px;height:630px;
    display:flex;background:var(--paper);
    box-shadow:0 2px 10px rgba(0,0,0,.12);
  }
  /* back cover */
  .back-cover{width:405px;height:100%;position:relative;padding:46px 40px 0}
  .divider{display:block;margin:0 auto 18px}
  .testimonial,.blurb{
    font-family:"EB Garamond",serif;font-size:13.5px;line-height:1.5;color:var(--body);text-align:justify
  }
  .testimonial cite{display:block;text-align:right;font-style:italic;margin-top:6px}
  .divider-second{margin-top:18px}
  .code-box{position:absolute;left:40px;bottom:40px;width:96px;height:70px;border:1px solid var(--ink);background:var(--paper)}
  /* spine */
  .spine{width:50px;height:100%;position:relative;border-left:1px solid var(--edge);border-right:1px solid var(--edge)}
  .spine-rule{position:absolute;top:40px;left:12px;width:26px;height:1px;background:var(--ink)}
  .spine-title{
    position:absolute;left:50%;top:70px;transform-origin:0 0;
    transform:rotate(90deg) translateY(-50%);
    white-space:nowrap;font-family:"Playfair Display",serif;font-weight:700;
    font-size:19px;letter-spacing:1px;color:var(--ink)
  }
  /* front cover */
  .front-cover{width:405px;height:100%;position:relative}
  .title{
    position:absolute;top:48px;left:0;right:0;text-align:center;
    font-family:"Playfair Display",serif;font-weight:900;color:var(--ink);
    font-size:62px;line-height:1.02;letter-spacing:-.5px;text-transform:uppercase
  }
  .title .title-small{display:block;font-size:50px}
  .band{
    position:absolute;left:0;right:0;bottom:0;height:280px;
    background:linear-gradient(var(--band-top),var(--band-bottom));
    text-align:center;color:var(--gold)
  }
  .band::before{content:"";position:absolute;top:0;left:0;right:0;height:4px;background:linear-gradient(90deg,var(--gold-deep),var(--gold),var(--gold-deep))}
  .tagline{
    margin-top:42px;font-family:"Cinzel",serif;font-weight:400;
    font-size:23px;line-height:1.3;text-transform:uppercase;padding:0 30px
  }
  .band-rule{width:300px;height:1px;margin:32px auto 0;background:var(--gold)}
  .author{
    margin-top:26px;font-family:"Cinzel",serif;font-weight:600;
    font-size:24px;letter-spacing:7px;text-transform:uppercase
  }
</style>
</head>
<body>
  <main class="cover-wrap">
    <section class="back-cover">
      <svg class="divider" width="140" height="8" viewBox="0 0 140 8"><line x1="0" y1="4" x2="140" y2="4" stroke="#161616" stroke-width="1"/><rect x="66" y="0" width="8" height="8" transform="rotate(45 70 4)" fill="#161616"/></svg>
      <p class="testimonial">This book changed the way I face hard seasons. Each chapter pairs a clear truth from scripture with simple findings from science, and the result is steady, practical hope. I finished it calmer, more focused and ready to act. I have already bought copies for my sister and for the women in my Bible study group at church.
        <cite>— Sample Reader</cite></p>
      <svg class="divider divider-second" width="140" height="8" viewBox="0 0 140 8"><line x1="0" y1="4" x2="140" y2="4" stroke="#161616" stroke-width="1"/><rect x="66" y="0" width="8" height="8" transform="rotate(45 70 4)" fill="#161616"/></svg>
      <p class="blurb">Walking Into Amber Light offers seven ways of thinking that help you move through loss, fear and change. Written with warmth and conviction, it invites you to trust God, renew your mind and take one faithful step at a time toward the life you were made to live.</p>
      <div class="code-box"></div>
    </section>

    <section class="spine">
      <span class="spine-rule"></span>
      <span class="spine-title">WALKING INTO AMBER LIGHT</span>
    </section>

    <section class="front-cover">
      <h1 class="title">Walking<span class="title-small">Into Amber</span>Light</h1>
      <div class="band">
        <p class="tagline">Seven Truths for Rising Above Life's Storms</p>
        <div class="band-rule"></div>
        <p class="author">Author Name</p>
      </div>
    </section>
  </main>
</body>
</html>
```